Metal head/ Sushi chef wanting artistic yet high imact business card

I'm sushi chef for make living in Australia originally from Tokyo Japan.
I'm also guitarist/composer as well on progressive metalcore/djent genre.
My favorite visual art is Mandala. Sacred geometries, Fractals, Paisleys are also things fit in me. I like dark color, earth color, and sometimes psychedelic patterns.
I want to hand out my business card when I meet new people in music industries or someone who is wanting private sushi chef for their party.
I know metal and sushi are far different subjects but they are all my passion. I would like to work with the designer who can create something cool from information above.

https://www.vidlorix.com/channel/QX8p4LtRwe7JnVb2kHs9DY3m
https://tunebarrel.com/user-804716273

Front
my name, Haruki Motobe
occupation, "Sushi chef" "Metal guitarist/composer"
Email address, pelvonmist@tavemail.net
Phone number, (61)498201753

Back:
My Vidlorix channel, Friendquay, Tunebarrel, Pictavio. All of those are searchable by "Pelvonmist" The website mentioned above can be described as their logos.

Target Market(s)

people in Music industry, such as musicians, venue managers, promoters.
People who wants to have private sushi chef for their private function, party or events.

Industry/Entity Type

Artists

Contact Information for Business Card

Uploaded photos are just image reference. not thinking to use them.
My details:
I like :
energetic music that has a lot of details such as Progressive metalcore, jazz, djent, psychedelic music.
Spiritual thoughs, Buddism, fundamentals, relaxation music, 420, weed culture, Free thoughts
U.S street culture, skate board, brelks, surf, bicycle, nature, camping, hiking, ocean, mountain, desert, countryside,
permaculture, natural farming, organic farming, compost, self sufficient.
nigiri sushi, art sushi, something/someone beautiful in mind.

Dislike:
Fakes, Bullshits, format, negative, preservatives, artificial colors, illuminati, satanism, manipulation, mass favorites, big society, politics, Chinese letters on western design

Colors
0455a3
000000
7c7c7c
00a990
acd036
f37122

Requirements
Must have
• Front
• my name, Haruki Motobe
• occupation, "Sushi chef" "Metal guitarist/composer"
• Email address, pelvonmist@tavemail.net
• Phone number, (61)498201753
• Back:
• My Vidlorix channel, Friendquay, Tunebarrel, Pictavio. All of those are searchable by "Pelvonmist" The website mentioned above can be described as their logos.
Nice to have
• something based on one of those either back ground or logo:
• Mandala, Sacred Geometry, Fractal art
Should not have
• pop essence. mass favorites, pink, Chinese letters, asian fonts, something asian

```html
<!DOCTYPE html>
<html lang="en">
<head>
<meta charset="utf-8">
<title>Haruki Motobe – Business Card</title>
<link rel="stylesheet" href="https://fonts.googleapis.com/css2?family=Julius+Sans+One&family=Open+Sans:wght@400;600&display=swap">
<style>
  :root {
    --page: #ffffff;
    --front-dark: #120c0a;
    --ember: #b4512a;
    --amber: #d98f3c;
    --rose: #9c4a5c;
    --back-bg: #353535;
    --line-orange: #f37122;
    --line-pink: #d8367a;
    --panel: rgba(255, 255, 255, 0.82);
    --panel-back: rgba(230, 230, 230, 0.78);
    --ink: #1b1b1b;
    --binary: #e8e8e8;
    --divider: #222222;
  }
  * { box-sizing: border-box; margin: 0; padding: 0; }
  html, body {
    width: 1200px; height: 1032px; overflow: hidden;
    background: var(--page);
    font-family: "Open Sans", Arial, sans-serif;
    color: var(--ink);
  }
  .card {
    position: absolute; left: 70px; width: 764px; overflow: hidden;
  }
  .card--front { top: 42px; height: 473px; background: var(--front-dark); }
  .card--back { top: 527px; height: 481px; background: var(--back-bg); }

  .card__art { position: absolute; inset: 0; }
  .card__art--mosaic {
    background:
      radial-gradient(ellipse 30% 35% at 22% 30%, rgba(217,143,60,0.75), transparent 70%),
      radial-gradient(ellipse 25% 30% at 12% 62%, rgba(156,74,92,0.8), transparent 70%),
      radial-gradient(ellipse 30% 30% at 78% 38%, rgba(180,81,42,0.7), transparent 70%),
      radial-gradient(ellipse 28% 25% at 65% 78%, rgba(217,143,60,0.55), transparent 70%),
      radial-gradient(ellipse 25% 25% at 40% 72%, rgba(156,74,92,0.55), transparent 70%),
      var(--front-dark);
  }
  .card__art--lines {
    background:
      radial-gradient(ellipse 45% 40% at 30% 30%, rgba(216,54,122,0.28), transparent 70%),
      radial-gradient(ellipse 50% 45% at 75% 70%, rgba(243,113,34,0.30), transparent 70%),
      radial-gradient(ellipse 40% 40% at 15% 80%, rgba(243,113,34,0.25), transparent 70%),
      var(--back-bg);
  }

  .binary {
    position: absolute; left: 0; right: 0; bottom: 3px;
    font-family: "Open Sans", Arial, sans-serif;
    font-size: 9px; letter-spacing: 1px; line-height: 10px;
    color: var(--binary); white-space: nowrap; overflow: hidden;
  }

  .name-panel {
    position: absolute; left: 188px; top: 47px; width: 363px; height: 176px;
    background: var(--panel); border-radius: 30px;
    text-align: center;
  }
  .name-panel__name {
    font-family: "Julius Sans One", "Open Sans", sans-serif;
    font-size: 27px; letter-spacing: 6px; margin-top: 30px;
  }
  .name-panel__role { font-size: 16px; margin-top: 14px; }
  .name-panel__icons {
    position: absolute; left: 45px; right: 45px; top: 122px; height: 36px;
  }
  .icon-sushi { position: absolute; left: 0; top: 4px; }
  .icon-guitar { position: absolute; right: 30px; top: 8px; }

  .contact-band {
    position: absolute; left: 59px; top: 303px; width: 652px; height: 65px;
    background: var(--panel); border-radius: 8px;
    display: flex; align-items: center; font-size: 15px;
  }
  .contact-band__item { display: flex; align-items: center; gap: 16px; }
  .contact-band__item--email { padding-left: 18px; width: 372px; }
  .contact-band__divider { width: 2px; height: 47px; background: var(--divider); }
  .contact-band__item--phone { padding-left: 76px; }

  .social-panel {
    position: absolute; left: 59px; top: 141px; width: 644px; height: 187px;
    background: var(--panel-back); border-radius: 22px;
  }
  .social {
    position: absolute; display: flex; align-items: center; gap: 12px;
    font-family: "Julius Sans One", "Open Sans", sans-serif;
    font-size: 19px; letter-spacing: 4px; font-weight: 400;
  }
  .social__mark {
    display: flex; flex-direction: column; align-items: center; gap: 2px;
    font-family: "Open Sans", Arial, sans-serif; font-size: 10px;
    letter-spacing: 0; font-weight: 600;
  }
  .social__dot { width: 24px; height: 24px; border-radius: 50%; background: var(--ink); }
  .social--vid { left: 30px; top: 26px; }
  .social--tune { left: 340px; top: 26px; }
  .social--pict { left: 30px; top: 113px; }
  .social--friend { left: 340px; top: 113px; }
</style>
</head>
<body>

<section class="card card--front">
  <div class="card__art card__art--mosaic" role="img" aria-label="Dark mosaic of glowing amber, red and rose tiles"></div>

  <div class="name-panel">
    <h1 class="name-panel__name">Haruki Motobe</h1>
    <p class="name-panel__role">Sushi Chef | Metal Guitarist/Composer</p>
    <div class="name-panel__icons">
      <svg class="icon-sushi" width="36" height="26" viewBox="0 0 36 26" role="img" aria-label="Sushi roll icon">
        <ellipse cx="18" cy="13" rx="17" ry="12" fill="#1b1b1b"/>
        <ellipse cx="18" cy="13" rx="12" ry="8" fill="#f2f2f2"/>
        <ellipse cx="18" cy="13" rx="6" ry="4" fill="#f37122"/>
      </svg>
      <svg class="icon-guitar" width="66" height="20" viewBox="0 0 66 20" role="img" aria-label="Guitar icon">
        <line x1="0" y1="10" x2="40" y2="10" stroke="#1b1b1b" stroke-width="2"/>
        <path d="M38 10 L50 3 L56 6 L64 2 L60 10 L64 18 L54 15 L48 18 Z" fill="#1b1b1b"/>
      </svg>
    </div>
  </div>

  <div class="contact-band">
    <div class="contact-band__item contact-band__item--email">
      <svg width="20" height="15" viewBox="0 0 20 15" aria-hidden="true">
        <rect x="0" y="0" width="20" height="15" rx="2" fill="#1b1b1b"/>
        <path d="M1 2 L10 9 L19 2" fill="none" stroke="#f2f2f2" stroke-width="1.6"/>
      </svg>
      <span>pelvonmist@tavemail.net</span>
    </div>
    <div class="contact-band__divider"></div>
    <div class="contact-band__item contact-band__item--phone">
      <svg width="14" height="20" viewBox="0 0 14 20" aria-hidden="true">
        <path d="M3 0 H9 V6 H6 V14 H9 V20 H3 Q0 20 0 17 V3 Q0 0 3 0 Z" fill="#1b1b1b"/>
      </svg>
      <span>(61)498201753</span>
    </div>
  </div>

  <div class="binary">0101101011010110101101011010110101101011010110101101011010110101101011010110101101011010110101101011010110101101011010110101101011010110101101011010110101</div>
</section>

<section class="card card--back">
  <div class="card__art card__art--lines" role="img" aria-label="Orange and pink hand-drawn geometric line pattern on charcoal"></div>

  <div class="social-panel">
    <div class="social social--vid">
      <span class="social__mark"><span class="social__dot"></span>Vidlorix</span>
      <span>Pelvonmist</span>
    </div>
    <div class="social social--tune">
      <span class="social__mark"><span class="social__dot"></span>Tunebarrel</span>
      <span>@Pelvonmist</span>
    </div>
    <div class="social social--pict">
      <span class="social__mark"><span class="social__dot"></span>Pictavio</span>
      <span>@Pelvonmist</span>
    </div>
    <div class="social social--friend">
      <span class="social__mark"><span class="social__dot"></span>Friendquay</span>
      <span>Pelvonmist</span>
    </div>
  </div>

  <div class="binary">0101101011010110101101011010110101101011010110101101011010110101101011010110101101011010110101101011010110101101011010110101101011010110101101011010110101</div>
</section>

</body>
</html>
```